Non-Fiction Book On Creativity - Cover Design / Physical and E-Book

I am looking for designs for my first book! It's called: Patience Builds Harbors. The subtitle is: 12 Chapters About Gathering Courage, Mending Fences, And Walking A Quiet Road.
It's a series of short lessons and principals on creativity and it will be a Vellora book and a physical book.
I'm really open to any type of designs but have attached some screenshots of other book covers that have a design and style that I like.
Please let me know if you have any questions or need any more information.
Creativity / Self-Help / Personal Development

```html
<!DOCTYPE html>
<html lang="en">
<head>
<meta charset="utf-8">
<title>Patience Builds Harbors — Book Cover</title>
<link rel="stylesheet" href="https://fonts.googleapis.com/css2?family=Bebas+Neue&family=Montserrat:wght@400&family=Tinos&display=swap">
<style>
  :root {
    --backdrop: #a7a7a7;
    --paper: #ffffff;
    --cover-red: #d9141c;
    --cover-red-soft: #ee6a6e;
    --title-blue: #1366b1;
    --title-black: #0c0c0c;
    --title-red: #d3102d;
    --art-tone: #7a6a52;
  }
  * { box-sizing: border-box; margin: 0; padding: 0; }
  html, body {
    width: 1200px; height: 800px; overflow: hidden;
    background: var(--backdrop);
  }
  .stage {
    width: 1200px; height: 800px;
    display: flex; align-items: center; justify-content: center;
  }
  .cover {
    position: relative;
    width: 470px; height: 740px;
    background: var(--paper);
    overflow: hidden;
  }
  .cover-art {
    position: absolute; left: 60px; top: 300px;
    width: 350px; height: 320px;
    background: radial-gradient(ellipse at 50% 50%, var(--art-tone) 0%, rgba(122,106,82,0.55) 45%, rgba(122,106,82,0) 72%);
    z-index: 0;
  }
  .cover-bands { position: absolute; inset: 0; width: 100%; height: 100%; z-index: 1; }
  .author {
    position: absolute; top: 26px; left: 0; right: 0;
    text-align: center;
    font-family: "Montserrat", sans-serif;
    font-size: 23px; letter-spacing: 5px;
    color: var(--paper);
    z-index: 2;
  }
  .title {
    position: absolute; top: 118px; left: 0; width: 470px; height: 230px;
    transform: rotate(-7deg);
    transform-origin: 50% 50%;
    font-family: "Bebas Neue", sans-serif;
    font-weight: 400;
    line-height: 0.8;
    z-index: 2;
  }
  .title span { position: absolute; white-space: nowrap; }
  .title-line-one { left: 40px; top: 24px; font-size: 84px; color: var(--title-blue); }
  .title-line-two { left: 236px; top: 88px; font-size: 84px; color: var(--title-black); }
  .title-line-three { left: 64px; top: 146px; font-size: 124px; color: var(--title-red); }
  .subtitle {
    position: absolute; left: 34px; right: 34px; top: 646px;
    text-align: center;
    font-family: "Tinos", serif;
    font-size: 18px; line-height: 1.15;
    text-transform: uppercase;
    color: var(--paper);
    z-index: 2;
  }
</style>
</head>
<body>
<main class="stage">
  <article class="cover">
    <div class="cover-art" role="img" aria-label="Illustration area: painterly collage of a blindfolded figure surrounded by rust, olive and grey paint splashes and flying birds"></div>

    <svg class="cover-bands" viewBox="0 0 470 740" preserveAspectRatio="none" aria-hidden="true">
      <defs>
        <linearGradient id="top-band-fade" x1="0" y1="0" x2="0" y2="1">
          <stop offset="0" stop-color="var(--cover-red)"/>
          <stop offset="0.6" stop-color="var(--cover-red)"/>
          <stop offset="1" stop-color="var(--cover-red-soft)"/>
        </linearGradient>
        <linearGradient id="bottom-band-fade" x1="0" y1="0" x2="0" y2="1">
          <stop offset="0" stop-color="var(--cover-red-soft)"/>
          <stop offset="0.35" stop-color="var(--cover-red)"/>
          <stop offset="1" stop-color="var(--cover-red)"/>
        </linearGradient>
      </defs>
      <path class="band-top" fill="url(#top-band-fade)"
        d="M0 0H470V128L452 132 440 124 420 130 402 122 380 128 360 118 338 126 318 116 300 124 282 114 262 120 246 108 226 112 210 104 192 100 176 106 160 98 140 104 124 112 108 108 90 118 72 112 54 126 36 122 18 134 0 130Z"/>
      <path class="band-bottom" fill="url(#bottom-band-fade)"
        d="M0 612L16 618 34 610 52 620 70 614 92 624 112 616 134 622 156 612 180 620 204 626 228 632 250 636 270 628 292 622 314 614 336 620 356 612 378 618 398 610 420 616 440 608 458 614 470 610V740H0Z"/>
    </svg>

    <p class="author">BY AUTHORS NAME</p>

    <h1 class="title">
      <span class="title-line-one">PATIENCE</span>
      <span class="title-line-two">BUILDS</span>
      <span class="title-line-three">HARBORS</span>
    </h1>

    <p class="subtitle">12 Chapters About Gathering Courage, Mending Fences, And Walking A Quiet Road</p>
  </article>
</main>
</body>
</html>
```